Venue Booking Site

I would like a venue directory and booking website designed. The idea is that end users will come to the site to find venues for weddings, parties, events etc. They will be able to find the venue based on many criteria, the most important ones are availability and location - they will be able to see in real time which venues are available for the desired dates and areas.

Venues will be able to use the website as a reservation management tool, receive payments for bookings through the site and be able to manage bookings on the go. This will be made into an app. It needs to be developed in bootstrap. Brand name to be used: Pinevault. Venue, place and space bookings.

Target audience - end users - anyone who is looking for a venue. For Community members it will provide an easy way to find a suitable venue
Outline what dates and times the venue is available
Outline costs involved in booking the venue
Search via many other criteria
It will allow the customer to book and pay for the venue online in one smooth process

Clients: Venue managers - particularly focussing on not for profit businesses eg, GPWs, community hall managers, small business managers. These people typically use paper based systems yet and do not use websites so it needs to be very user friendly. Future growth to restaurants, pubs, event venues who have a stronger familiarity with computers and who might already use their own booking management tool - so this needs to be able to link in with their system.

What need will this meet for venue managers:
This tool provides venues with greater visibility, promotion and advertising of their venue
This allows more customers to find them and book with them
This tool will be offered to not-for-profit venue managers for free to better connect them to the community
This means greater profit for these community venues
This means more revenue and jobs created in these communities

Sample of the layout / contents attached. This is not a complete site map as yet as it is a work in progress for final pages.

Industry/Entity Type

Small Business

Number of Pages Required

5+ page

Font styles to use
Sans Serif

Colors
eb2027

Requirements
Must have
• This is a psd file only - one template for each different section, home page, search page, detailed page view, admin back end
Should not have
• does not need to be coded.
• Note, the lantern quay logo jpeg files were files we were toying with using for this project- but I am happy to use the main pinevault logo- I will let you decide.

```html
<!DOCTYPE html>
<html lang="en">
<head>
<meta charset="utf-8">
<title>Pinevault – Venue Bookings</title>
<link rel="stylesheet" href="https://fonts.googleapis.com/css2?family=Raleway:wght@400;500;600;700&display=swap">
<style>
:root{
  --red:#eb2027;
  --ink:#4a4a4a;
  --muted:#8a8a8a;
  --line:#e2e2e2;
  --panel:#f7f7f7;
  --field:#ffffff;
  --star:#f5b800;
  --map-water:#9ec9f0;
  --map-land:#f1ede4;
  --photo-warm:#b36a22;
}
*{box-sizing:border-box;margin:0;padding:0}
html,body{width:683px;height:1200px;overflow:hidden}
body{position:relative;font-family:"Raleway",sans-serif;color:var(--ink);background:#fff;font-size:7px}
.abs{position:absolute}

/* header */
.site-header{position:absolute;left:0;top:0;width:683px;height:72px;background:#fff}
.brand{position:absolute;left:50px;top:18px;display:flex;align-items:center;gap:6px;font-size:24px;font-weight:600;color:var(--red);letter-spacing:-.5px}
.brand-mark{width:12px;height:12px;background:var(--red);border-radius:2px}
.support{position:absolute;left:369px;top:15px;display:flex;gap:5px;align-items:center}
.support-icon{width:15px;height:15px;border-radius:50%;background:var(--red)}
.support small{display:block;font-size:7px;color:var(--ink);line-height:1}
.support strong{display:block;font-size:9px;color:var(--red);font-weight:700}
.site-search{position:absolute;left:467px;top:17px;width:110px;height:16px;border:1px solid var(--line);border-radius:8px;font-size:5.5px;color:#aaa;padding:4px 8px}
.tool{position:absolute;top:19px;width:12px;height:12px}
.key-btn{position:absolute;left:617px;top:16px;width:17px;height:17px;border:1.5px solid var(--red);border-radius:50%}
.main-nav{position:absolute;left:194px;top:43px;display:flex;gap:0;font-size:8.5px}
.main-nav a{color:var(--ink);text-decoration:none;padding:4px 8px;margin-right:16px;border-radius:10px}
.main-nav a.active{color:var(--red);font-weight:700;border:1px solid var(--line)}
.login-panel{position:absolute;left:521px;top:40px;width:112px;height:67px;background:#fff;box-shadow:0 1px 4px rgba(0,0,0,.2);z-index:5;padding:8px 9px}
.login-panel .input{height:11px;border:1px solid var(--line);border-radius:6px;font-size:5px;color:#aaa;padding:2px 6px;margin-bottom:4px}
.login-row{display:flex;justify-content:space-between;align-items:center;margin-top:2px}
.login-row label{font-size:5px;color:#aaa;display:flex;align-items:center;gap:3px;line-height:1}
.login-row label i{width:7px;height:7px;border:1px solid var(--line)}
.btn{background:var(--red);color:#fff;font-weight:700;text-align:center;border-radius:12px;text-transform:uppercase}
.login-row .btn{width:47px;height:11px;font-size:5.5px;line-height:11px}

/* map */
.map{position:absolute;left:0;top:72px;width:683px;height:215px;background:linear-gradient(135deg,var(--map-water),var(--map-land) 45%,var(--map-land) 60%,var(--map-water));border-top:2px solid var(--red);border-bottom:2px solid var(--red)}

/* search */
.search{position:absolute;left:0;top:287px;width:683px;height:135px;background:linear-gradient(#fff,#f2f2f2)}
.step{position:absolute;top:22px;width:140px}
.step h3{font-size:9px;font-weight:600;color:var(--ink);margin-bottom:14px}
.step h3 b{color:var(--red)}
.field-label{font-size:5.5px;font-weight:700;text-transform:uppercase;margin-bottom:5px}
.field{height:16px;border:1px solid var(--line);background:var(--field);border-radius:8px;font-size:5.5px;color:#aaa;padding:4px 7px;position:relative}
.radio{display:flex;align-items:center;gap:5px;font-size:6px;color:var(--muted);position:absolute}
.radio i{width:10px;height:10px;border:1px solid #ccc;border-radius:50%}
.search-btn{position:absolute;left:260px;top:104px;width:163px;height:25px;line-height:25px;font-size:8.5px}

/* venues */
.section-title{position:absolute;left:0;width:683px;text-align:center;color:var(--red);font-size:18px;font-weight:400;text-transform:uppercase}
.rule{position:absolute;left:49px;width:585px;height:1px;background:var(--line)}
.venues-bg{position:absolute;left:0;top:422px;width:683px;height:346px;background:#fafafa}
.card{position:absolute;top:485px;width:142px;height:240px;background:#fff;box-shadow:0 1px 3px rgba(0,0,0,.15)}
.card-photo{height:83px;background:linear-gradient(#6b3a1a,var(--photo-warm) 55%,#7a2a18)}
.card-body{padding:8px 7px}
.card-top{display:flex;justify-content:space-between;align-items:center}
.card-top h4{font-size:8.5px;color:var(--red);font-weight:700}
.stars{color:var(--star);font-size:7.5px;letter-spacing:-.5px}
.stars span{color:#ccc}
.card-meta{display:flex;justify-content:space-between;font-size:6px;color:var(--muted);margin-top:3px;padding-bottom:6px;border-bottom:1px solid var(--line)}
.card-price{display:flex;justify-content:space-between;font-size:6.3px;padding:5px 0;border-bottom:1px solid var(--line)}
.card-price b{font-size:7.5px}
.card-text{font-size:6.2px;line-height:1.35;color:var(--muted);margin-top:7px}
.card-text a{color:var(--red);text-decoration:none}
.card .btn{position:absolute;left:35px;top:230px;width:72px;height:18px;line-height:18px;font-size:8px}

/* reasons */
.reason{position:absolute;width:142px;height:83px;background:#f7f7f7;border:1px solid #ececec;padding:10px 7px}
.reason h5{font-size:8px;font-weight:600;color:var(--muted);padding-bottom:5px;border-bottom:1px solid var(--line);margin-bottom:4px}
.reason p{font-size:6.2px;line-height:1.35;color:var(--muted)}

/* footer */
.site-footer{position:absolute;left:0;top:1032px;width:683px;height:116px;background:#f5f5f5}
.foot-col{position:absolute;top:16px;width:130px}
.foot-col h6{font-size:8px;font-weight:600;padding-bottom:5px;border-bottom:1px solid var(--line);margin-bottom:6px}
.foot-col li{list-style:none;font-size:6.3px;color:var(--muted);margin-bottom:4px;display:flex;align-items:center;gap:4px}
.social{display:flex;flex-wrap:wrap;gap:4px;width:130px}
.social i{width:14px;height:14px;background:#cfcfcf;border-radius:2px}
.social i.on{background:#3b5b98}
.newsletter{display:flex;align-items:center}
.newsletter .field{width:90px;font-size:5.5px}
.newsletter .btn{width:47px;height:17px;line-height:17px;font-size:6.5px;margin-left:-6px}
.bottom-bar{position:absolute;left:49px;top:1170px;width:585px;display:flex;justify-content:space-between;font-size:6.5px;color:var(--muted)}
.bottom-bar nav{display:flex;gap:22px}
.bottom-bar nav a{color:var(--ink);text-decoration:none}
.bottom-bar nav a.active{color:var(--red);font-weight:700}
</style>
</head>
<body>

<header class="site-header">
  <div class="brand"><span class="brand-mark"></span>pinevault</div>
  <div class="support"><span class="support-icon"></span><div><small>24/7 Support</small><strong>01 40 55 62 18</strong></div></div>
  <div class="site-search">Search entire site</div>
  <svg class="tool" style="left:583px" viewBox="0 0 12 12"><path d="M2 6 6 2 10 6V10H7V7H5V10H2Z" fill="#888"/></svg>
  <svg class="tool" style="left:601px" viewBox="0 0 12 12"><path d="M2 3H10M2 6H10M2 9H10" stroke="#888" stroke-width="1.4"/></svg>
  <div class="key-btn"><svg viewBox="0 0 17 17" width="14" height="14"><circle cx="5" cy="7" r="2" fill="none" stroke="#eb2027" stroke-width="1.3"/><path d="M7 7H12M11 7V9" stroke="#eb2027" stroke-width="1.3"/></svg></div>
  <nav class="main-nav">
    <a class="active" href="#">Home</a><a href="#">Venues</a><a href="#">News &amp; Offers</a><a href="#">Inspiration</a><a href="#">Services</a>
  </nav>
  <form class="login-panel">
    <div class="input">Username</div>
    <div class="input">Password</div>
    <div class="login-row"><label><i></i>Save<br>password</label><div class="btn">Login</div></div>
  </form>
</header>

<div class="map" role="img" aria-label="City map with venue location pins showing hotel photos and star ratings"></div>

<section class="search">
  <div class="step" style="left:56px">
    <h3><b>#1:</b> What?</h3>
    <div class="radio" style="left:0;top:32px"><i></i>Hotel</div>
    <div class="radio" style="left:64px;top:32px"><i></i>Self Catering</div>
    <div class="radio" style="left:0;top:52px"><i></i>Rent a Car</div>
    <div class="radio" style="left:64px;top:52px"><i></i>Tour</div>
  </div>
  <div class="step" style="left:202px">
    <h3><b>#2:</b> Where?</h3>
    <div class="field-label">Your destination</div>
    <div class="field">City, Region etc</div>
  </div>
  <div class="step" style="left:348px">
    <h3><b>#3:</b> When?</h3>
    <div style="display:flex;gap:4px">
      <div style="width:66px"><div class="field-label">Check-in date</div><div class="field">dd/mm/yy</div></div>
      <div style="width:66px"><div class="field-label">Check-out date</div><div class="field">dd/mm/yy</div></div>
    </div>
  </div>
  <div class="step" style="left:494px">
    <h3><b>#4:</b> Who?</h3>
    <div class="field-label">Rooms</div>
    <div class="field">Rooms</div>
  </div>
  <div class="btn search-btn">Search</div>
</section>

<div class="venues-bg"></div>
<h2 class="section-title" style="top:448px">Top Venues</h2>
<div class="rule" style="top:475px"></div>

<article class="card" style="left:49px">
  <div class="card-photo" role="img" aria-label="Grand hotel lobby with chandelier"></div>
  <div class="card-body">
    <div class="card-top"><h4>Prime Apartment</h4><span class="stars">★★★★<span>★</span></span></div>
    <div class="card-meta"><span>Venace » Show map</span><span>8 /10</span></div>
    <div class="card-price"><span>Price per room per night from</span><b>$ 500</b></div>
    <p class="card-text">Lorem ipsum dolor sit amet, consectetuer adipiscing elit, sed diam nonummy nibh euismod tincidunt ut laoreet dolore magna aliquam erat volutpat. Ut wisi enim ad minim veniam, quis nostrud exerci tation ullamcorper suscipit ... <a href="#">Read more...</a></p>
  </div>
  <div class="btn">Book Now</div>
</article>
<article class="card" style="left:196px">
  <div class="card-photo" role="img" aria-label="Grand hotel lobby with chandelier"></div>
  <div class="card-body">
    <div class="card-top"><h4>Prime Apartment</h4><span class="stars">★★★★<span>★</span></span></div>
    <div class="card-meta"><span>Venace » Show map</span><span>8 /10</span></div>
    <div class="card-price"><span>Price per room per night from</span><b>$ 500</b></div>
    <p class="card-text">Lorem ipsum dolor sit amet, consectetuer adipiscing elit, sed diam nonummy nibh euismod tincidunt ut laoreet dolore magna aliquam erat volutpat. Ut wisi enim ad minim veniam, quis nostrud exerci tation ullamcorper suscipit ... <a href="#">Read more...</a></p>
  </div>
  <div class="btn">Book Now</div>
</article>
<article class="card" style="left:344px">
  <div class="card-photo" role="img" aria-label="Grand hotel lobby with chandelier"></div>
  <div class="card-body">
    <div class="card-top"><h4>Prime Apartment</h4><span class="stars">★★★★<span>★</span></span></div>
    <div class="card-meta"><span>Venace » Show map</span><span>8 /10</span></div>
    <div class="card-price"><span>Price per room per night from</span><b>$ 500</b></div>
    <p class="card-text">Lorem ipsum dolor sit amet, consectetuer adipiscing elit, sed diam nonummy nibh euismod tincidunt ut laoreet dolore magna aliquam erat volutpat. Ut wisi enim ad minim veniam, quis nostrud exerci tation ullamcorper suscipit ... <a href="#">Read more...</a></p>
  </div>
  <div class="btn">Book Now</div>
</article>
<article class="card" style="left:491px">
  <div class="card-photo" role="img" aria-label="Grand hotel lobby with chandelier"></div>
  <div class="card-body">
    <div class="card-top"><h4>Prime Apartment</h4><span class="stars">★★★★<span>★</span></span></div>
    <div class="card-meta"><span>Venace » Show map</span><span>8 /10</span></div>
    <div class="card-price"><span>Price per room per night from</span><b>$ 500</b></div>
    <p class="card-text">Lorem ipsum dolor sit amet, consectetuer adipiscing elit, sed diam nonummy nibh euismod tincidunt ut laoreet dolore magna aliquam erat volutpat. Ut wisi enim ad minim veniam, quis nostrud exerci tation ullamcorper suscipit ... <a href="#">Read more...</a></p>
  </div>
  <div class="btn">Book Now</div>
</article>

<h2 class="section-title" style="top:797px">Why should you book your venue through Pinevault?</h2>
<div class="rule" style="top:825px"></div>

<div class="reason" style="left:49px;top:840px"><h5>Handpicked Hotels</h5><p>Lorem ipsum dolor sit amet, consectetuer adipiscing elit, sed diam nonummy nibh euismod tincidunt ut laoreet dolore magna aliquam erat volutpat.</p></div>
<div class="reason" style="left:196px;top:840px"><h5>Detailed Descriptions</h5><p>Ut wisi enim ad minim veniam, quis nostrud exerci tation ullamcorper suscipit ..</p></div>
<div class="reason" style="left:344px;top:840px"><h5>Handpicked Hotels</h5><p>Lorem ipsum dolor sit amet, consectetuer adipiscing elit, sed diam nonummy nibh euismod tincidunt ut laoreet dolore magna aliquam erat volutpat.</p></div>
<div class="reason" style="left:491px;top:840px"><h5>Detailed Descriptions</h5><p>Ut wisi enim ad minim veniam, quis nostrud exerci tation ullamcorper suscipit ..</p></div>
<div class="reason" style="left:49px;top:931px"><h5>Handpicked Hotels</h5><p>Lorem ipsum dolor sit amet, consectetuer adipiscing elit, sed diam nonummy nibh euismod tincidunt ut laoreet dolore magna aliquam erat volutpat.</p></div>
<div class="reason" style="left:196px;top:931px"><h5>Detailed Descriptions</h5><p>Ut wisi enim ad minim veniam, quis nostrud exerci tation ullamcorper suscipit ..</p></div>
<div class="reason" style="left:344px;top:931px"><h5>Handpicked Hotels</h5><p>Lorem ipsum dolor sit amet, consectetuer adipiscing elit, sed diam nonummy nibh euismod tincidunt ut laoreet dolore magna aliquam erat volutpat.</p></div>
<div class="reason" style="left:491px;top:931px"><h5>Detailed Descriptions</h5><p>Ut wisi enim ad minim veniam, quis nostrud exerci tation ullamcorper suscipit ..</p></div>

<footer class="site-footer">
  <div class="foot-col" style="left:56px">
    <h6>Pinevault Bookings</h6>
    <ul>
      <li><svg width="7" height="8" viewBox="0 0 7 8"><path d="M3.5 8 1 4A2.5 2.5 0 1 1 6 4Z" fill="#eb2027"/></svg>12 Alder Lane Harwood VIC</li>
      <li><svg width="7" height="7" viewBox="0 0 7 7"><path d="M1 1 3 1 3.5 2.5 2.5 3.3Q3.5 4.5 4 4.6L4.7 3.7 6 4.2 6 6Q2 6 1 1Z" fill="#eb2027"/></svg>03 5521 4706</li>
      <li><svg width="8" height="6" viewBox="0 0 8 6"><rect x=".5" y=".5" width="7" height="5" fill="none" stroke="#eb2027"/><path d="M.5 .5 4 3.5 7.5 .5" fill="none" stroke="#eb2027"/></svg>info@bookings.pinevault.com.au</li>
    </ul>
  </div>
  <div class="foot-col" style="left:203px">
    <h6>Support</h6>
    <ul><li>» Faq</li><li>» Make a Reservation</li><li>» Payment Options</li><li>» Booking Tips</li></ul>
  </div>
  <div class="foot-col" style="left:350px">
    <h6>Follow Us</h6>
    <div class="social"><i></i><i></i><i class="on"></i><i></i><i></i><i></i><i></i><i></i><i></i></div>
  </div>
  <div class="foot-col" style="left:497px">
    <h6>Newsletter</h6>
    <div class="newsletter"><div class="field">Email *</div><div class="btn">Signup</div></div>
  </div>
</footer>

<div class="bottom-bar">
  <span>Copyright © 2014 Pinevault. All Rights Reserved.</span>
  <nav><a class="active" href="#">Home</a><a href="#">Venues</a><a href="#">News &amp; Offers</a><a href="#">Inspiration</a><a href="#">Services</a><a href="#">Contact</a><a href="#">FAQs</a><a href="#">Terms&amp;Conditions</a></nav>
</div>

</body>
</html>
```